Communication and Marketing agency needs a new presentation card

We are a group of communication and marketing agencies specialized in companies that are in the logistics and industrial sector. The head agency is TELVANO Grupo and the group consists of 4 agencies: TELVANO Media, TELVANO Digital, TELVANO Research and EnlazaPorImagen. We hace 4 offices in Spain (Madrid, Barcelona, Valencia and Murcia). We are looking for a clean and attractive design that transmits our experience, brand presence in the market and knowledge to those who receive the card.It has to maintain the colors of the logo that is attached.
Target Market(s)
logistics and industrial sector
Marketing department
Clean and attractive design

```html
<!DOCTYPE html>
<html lang="en">
<head>
<meta charset="utf-8">
<title>TELVANO Grupo — Business Card</title>
<link href="https://fonts.googleapis.com/css2?family=Oswald:wght@600&family=Open+Sans:wght@400;600&display=swap" rel="stylesheet">
<style>
  :root {
    --stage: #1d1c1c;
    --card-back: #524e4b;
    --card-front: #f2f2f2;
    --brand-red: #b81c2a;
    --ink: #4a4644;
    --band: #524e4b;
    --white: #ffffff;
  }
  * { margin: 0; padding: 0; box-sizing: border-box; }
  html, body {
    width: 1200px; height: 900px; overflow: hidden;
    background: var(--stage);
    font-family: "Open Sans", Arial, sans-serif;
  }
  .canvas { position: relative; width: 1200px; height: 900px; }
  .card {
    position: absolute; left: 285px;
    width: 630px; height: 360px;
    overflow: hidden;
    box-shadow: 0 10px 30px rgba(0,0,0,.5);
  }
  .card--back { top: 50px; background: var(--card-back); }
  .card--front { top: 470px; background: var(--card-front); }

  .brand-name {
    font-family: "Open Sans", Arial, sans-serif;
    font-weight: 600;
    color: var(--brand-red);
    letter-spacing: 2px;
    white-space: nowrap;
  }
  .card--back .brand-name {
    position: absolute; left: 0; right: 0; top: 150px;
    text-align: center; font-size: 44px;
  }
  .card--front .brand-name {
    position: absolute; right: 50px; top: 44px;
    font-size: 30px;
  }

  .rule {
    position: absolute; left: 150px; right: 40px; top: 196px;
    height: 1px; background: var(--brand-red);
  }
  .person { position: absolute; left: 40px; top: 160px; }
  .person__name {
    font-family: "Oswald", Arial, sans-serif; font-weight: 600;
    font-size: 28px; color: var(--brand-red); line-height: 1.05;
    letter-spacing: .5px;
  }
  .person__role { font-size: 18px; color: var(--ink); line-height: 1.2; }

  .contact { position: absolute; left: 54px; top: 248px; list-style: none; }
  .contact li {
    display: flex; align-items: center; gap: 8px;
    font-size: 14px; color: var(--ink); line-height: 21px;
  }
  .contact svg { width: 12px; height: 12px; fill: var(--brand-red); }

  .office {
    position: absolute; right: 50px; top: 212px;
    text-align: left; font-size: 13px; color: var(--ink); line-height: 18px;
  }
  .office__web { color: var(--brand-red); font-weight: 600; font-size: 14px; }

  .footer-band {
    position: absolute; left: 0; right: 0; bottom: 0; height: 38px;
    background: var(--band);
  }
  .footer-accent {
    position: absolute; right: 40px; bottom: 0; width: 140px; height: 52px;
    background: var(--brand-red);
    border-left: 5px solid var(--card-front);
    border-right: 5px solid var(--card-front);
  }
</style>
</head>
<body>
<main class="canvas">
  <section class="card card--back" aria-label="Card back">
    <div class="brand-name">TELVANO Grupo</div>
  </section>

  <section class="card card--front" aria-label="Card front">
    <div class="brand-name">TELVANO Grupo</div>
    <div class="rule"></div>

    <div class="person">
      <div class="person__name">LUCAS FERRER</div>
      <div class="person__role">Founder</div>
    </div>

    <ul class="contact">
      <li>
        <svg viewBox="0 0 24 24" aria-hidden="true"><path d="M6.6 10.8a15 15 0 0 0 6.6 6.6l2.2-2.2a1 1 0 0 1 1-.25 11.4 11.4 0 0 0 3.6.57 1 1 0 0 1 1 1V20a1 1 0 0 1-1 1A17 17 0 0 1 3 4a1 1 0 0 1 1-1h3.5a1 1 0 0 1 1 1c0 1.25.2 2.45.57 3.6a1 1 0 0 1-.25 1z"/></svg>
        (000) 987-654-00
      </li>
      <li>
        <svg viewBox="0 0 24 24" aria-hidden="true"><path d="M2 5h20v14H2z M2 5l10 8 10-8" /></svg>
        info@telvanogroup.com
      </li>
    </ul>

    <div class="office">
      210-240 Calle Aurora,<br>
      MD 28014, Spain<br>
      <span class="office__web">telvanogroup.com</span>
    </div>

    <div class="footer-band"></div>
    <div class="footer-accent"></div>
  </section>
</main>
</body>
</html>
```